Bottle Water Design

I need the different sizes of water bottles with the labels
1. Cedar Hollow (round bottles) - 425ml, 650ml, 1.5L, 5L, and 5 gallon
2. Bright water (rectangle bottles) - 305ml, 500ml, 1.0L, 5L and 5 gallon
Updates

Low design quality

Target Market(s)

General Population

Requirements
Must have
• Different bottle sizea

```html
<!DOCTYPE html>
<html lang="en">
<head>
<meta charset="utf-8">
<title>Cedar Hollow – Bottle Range</title>
<link href="https://fonts.googleapis.com/css2?family=Josefin+Sans:wght@300&family=Open+Sans:wght@800&family=Tinos:wght@700&display=swap" rel="stylesheet">
<style>
  :root {
    --bg: #3ba635;
    --bg-glow: #5cb85a;
    --sky-top: #2b4d9e;
    --sky-mid: #2f62b4;
    --lake: #3e78c0;
    --forest: #1f5a32;
    --forest-dark: #143d24;
    --ink: #ffffff;
    --pet-clear: #d3e6ea;
    --pet-blue: #9fc3dc;
    --pet-edge: #7ea6cf;
    --cap: #5b9ad8;
    --cap-dark: #3f7fc2;
  }
  html, body {
    margin: 0;
    width: 1200px;
    height: 1200px;
    overflow: hidden;
  }
  .canvas {
    position: relative;
    width: 1200px;
    height: 1200px;
    background: radial-gradient(circle at 28% 48%, var(--bg-glow) 0%, var(--bg) 45%);
  }
  .bottles {
    position: absolute;
    inset: 0;
  }
  .pet-clear { fill: var(--pet-clear); fill-opacity: 0.92; stroke: var(--pet-edge); stroke-width: 1.5; }
  .pet-blue { fill: var(--pet-blue); fill-opacity: 0.95; stroke: var(--pet-edge); stroke-width: 1.5; }
  .cap { fill: var(--cap); }
  .collar { fill: var(--cap-dark); }
  .rib { stroke: var(--pet-edge); stroke-width: 2; fill: none; }
  .handle { fill: none; stroke: var(--cap); stroke-width: 7; stroke-linejoin: round; }

  .label {
    position: absolute;
    overflow: hidden;
    text-align: center;
    color: var(--ink);
  }
  .label-scene {
    position: absolute;
    inset: 0;
    background:
      linear-gradient(180deg,
        var(--sky-top) 0%,
        var(--sky-mid) 35%,
        var(--lake) 58%,
        var(--forest) 80%,
        var(--forest-dark) 100%);
  }
  .label-text {
    position: absolute;
    left: 0;
    right: 0;
  }
  .brand {
    margin: 0;
    font-family: "Josefin Sans", sans-serif;
    font-weight: 300;
    text-transform: uppercase;
    line-height: 0.95;
    letter-spacing: 0.02em;
  }
  .tagline {
    margin: 0;
    font-family: "Open Sans", sans-serif;
    font-weight: 800;
    text-transform: uppercase;
    letter-spacing: 0.04em;
    white-space: nowrap;
  }
  .volume {
    margin: 0;
    font-family: "Tinos", serif;
    font-weight: 700;
  }

  .label--bottle-a { left: 61px; top: 516px; width: 136px; height: 121px; }
  .label--bottle-b { left: 255px; top: 517px; width: 146px; height: 129px; }
  .label--gallon   { left: 444px; top: 513px; width: 315px; height: 216px; }
  .label--jug      { left: 868px; top: 600px; width: 219px; height: 129px; }

  .label--bottle-a .label-text,
  .label--bottle-b .label-text { top: 44px; }
  .label--bottle-a .brand,
  .label--bottle-b .brand { font-size: 19px; }
  .label--bottle-a .tagline,
  .label--bottle-b .tagline { font-size: 6.5px; margin-top: 5px; }
  .label--bottle-a .volume,
  .label--bottle-b .volume { font-size: 6px; margin-top: 4px; }

  .label--gallon .label-text { top: 80px; right: 110px; }
  .label--gallon .brand { font-size: 37px; }
  .label--gallon .tagline { font-size: 11px; margin-top: 10px; }
  .label--gallon .volume { font-size: 10px; margin-top: 10px; }
  .handle-window {
    position: absolute;
    left: 212px;
    top: 36px;
    width: 56px;
    height: 144px;
    border-radius: 10px;
    background: var(--bg);
  }

  .label--jug .label-text { top: 26px; }
  .label--jug .brand { font-size: 29px; }
  .label--jug .tagline { font-size: 10px; margin-top: 10px; }
  .label--jug .volume { font-size: 9px; margin-top: 8px; }
</style>
</head>
<body>
<main class="canvas">

  <svg class="bottles" width="1200" height="1200" viewBox="0 0 1200 1200" aria-hidden="true">
    <!-- 1.5 L round bottle -->
    <g class="bottle bottle--tall">
      <path class="pet-clear" d="M112 404 C72 440 61 480 61 516 L61 822 C61 840 70 850 82 850 L176 850 C190 850 197 840 197 822 L197 516 C197 480 186 440 146 404 Z"/>
      <rect class="collar" x="104" y="398" width="50" height="6" rx="2"/>
      <rect class="cap" x="107" y="364" width="44" height="34" rx="3"/>
    </g>
    <!-- 650 ml round bottle -->
    <g class="bottle bottle--slim">
      <path class="pet-clear" d="M312 404 C292 450 262 480 255 517 L255 822 C255 840 264 850 276 850 L380 850 C394 850 401 840 401 822 L401 517 C394 480 364 450 344 404 Z"/>
      <rect class="collar" x="304" y="400" width="48" height="6" rx="2"/>
      <rect class="cap" x="307" y="367" width="42" height="33" rx="3"/>
    </g>
    <!-- 5 gallon dispenser bottle -->
    <g class="bottle bottle--gallon">
      <path class="pet-blue" d="M574 330 L574 380 C540 408 476 414 456 430 L444 440 L444 820 C444 835 455 842 470 842 L733 842 C748 842 759 835 759 820 L759 440 L747 430 C727 414 660 408 628 380 L628 330 Z"/>
      <rect class="pet-blue" x="568" y="279" width="65" height="52" rx="4"/>
      <rect class="collar" x="570" y="309" width="61" height="8" rx="2"/>
      <line class="rib" x1="444" y1="458" x2="759" y2="458"/>
      <line class="rib" x1="444" y1="790" x2="759" y2="790"/>
    </g>
    <!-- 5 L jug -->
    <g class="bottle bottle--jug">
      <path class="handle" d="M924 458 L918 398 L958 388 L1000 388 L1036 398 L1030 458"/>
      <path class="pet-blue" d="M950 468 L885 540 C871 555 868 570 868 590 L868 825 C868 838 878 842 892 842 L1063 842 C1077 842 1087 838 1087 825 L1087 590 C1087 570 1084 555 1070 540 L1005 468 Z"/>
      <rect class="collar" x="938" y="458" width="77" height="10" rx="2"/>
      <rect class="cap" x="945" y="415" width="64" height="43" rx="4"/>
      <line class="rib" x1="868" y1="760" x2="1087" y2="760"/>
      <line class="rib" x1="868" y1="795" x2="1087" y2="795"/>
    </g>
  </svg>

  <section class="label label--bottle-a">
    <div class="label-scene" role="img" aria-label="Mountain lake landscape with evergreen forest under a blue sky"></div>
    <div class="label-text">
      <p class="brand">Cedar<br>Hollow</p>
      <p class="tagline">Purified spring water</p>
      <p class="volume">1.5L</p>
    </div>
  </section>

  <section class="label label--bottle-b">
    <div class="label-scene" role="img" aria-label="Mountain lake landscape with evergreen forest under a blue sky"></div>
    <div class="label-text">
      <p class="brand">Cedar<br>Hollow</p>
      <p class="tagline">Purified spring water</p>
      <p class="volume">650ml</p>
    </div>
  </section>

  <section class="label label--gallon">
    <div class="label-scene" role="img" aria-label="Mountain lake landscape with evergreen forest under a blue sky"></div>
    <div class="label-text">
      <p class="brand">Cedar<br>Hollow</p>
      <p class="tagline">Purified spring water</p>
      <p class="volume">5 gallon</p>
    </div>
    <div class="handle-window"></div>
  </section>

  <section class="label label--jug">
    <div class="label-scene" role="img" aria-label="Mountain lake landscape with evergreen forest under a blue sky"></div>
    <div class="label-text">
      <p class="brand">Cedar<br>Hollow</p>
      <p class="tagline">Purified spring water</p>
      <p class="volume">5L</p>
    </div>
  </section>

</main>
</body>
</html>
```